Plumber needs a business card

I need a new business card for my plumbing business. I dont have a logo at the moment but I want business cards that are simple but very professional. I want to look like
Name: Mitch Dorley
Address: (just make one up)
Phone: 0455 318 726
Email: mitch@dorleymail.com
Colors to use:
Blacks, blues, silvers

```html
<!DOCTYPE html>
<html lang="en">
<head>
<meta charset="utf-8">
<title>Dorley Plumbing – Business Card</title>
<link rel="stylesheet" href="https://fonts.googleapis.com/css2?family=Open+Sans:wght@400;600;700&display=swap">
<style>
  :root {
    --backdrop: #3a3a3a;
    --card-white: #ffffff;
    --band-dark: #0d1014;
    --band-mid: #1b2026;
    --stripe-deep: #1c4f8f;
    --stripe-light: #2a9fd8;
    --accent-blue: #2a9fd6;
    --text-light: #f2f4f6;
    --wordmark: #2e3135;
    --divider: #2b3037;
  }
  * { box-sizing: border-box; margin: 0; padding: 0; }
  html, body {
    width: 1200px; height: 750px; overflow: hidden;
    background: var(--backdrop);
    font-family: "Open Sans", Arial, sans-serif;
  }
  .business-card {
    position: absolute; left: 100px; top: 88px;
    width: 1000px; height: 573px;
    background: var(--card-white);
    border-radius: 34px; overflow: hidden;
    box-shadow: 0 10px 28px rgba(0,0,0,.45);
  }
  .brand-area {
    position: absolute; left: 0; top: 0; width: 100%; height: 298px;
    display: flex; align-items: center; justify-content: center; gap: 28px;
  }
  .brand-dot {
    width: 96px; height: 96px; border-radius: 50%;
    background: var(--accent-blue);
  }
  .brand-name {
    color: var(--wordmark); font-weight: 700;
    font-size: 64px; line-height: 1.05; letter-spacing: 1px;
  }
  .accent-stripe {
    position: absolute; top: 298px; left: 0; width: 100%; height: 17px;
    display: flex;
  }
  .accent-stripe .deep { flex: 1; background: var(--stripe-deep); }
  .accent-stripe .light { flex: 1; background: var(--stripe-light); }
  .info-band {
    position: absolute; top: 315px; left: 0; width: 100%; height: 258px;
    background: linear-gradient(160deg, var(--band-mid), var(--band-dark) 60%, #14202c);
  }
  .band-divider {
    position: absolute; left: 500px; top: 22px; width: 3px; height: 214px;
    background: var(--divider);
  }
  .person {
    position: absolute; left: 0; width: 500px; top: 72px; text-align: center;
  }
  .person-name { color: var(--accent-blue); font-size: 37px; line-height: 1.1; }
  .person-role { color: var(--text-light); font-size: 26px; line-height: 1.2; }
  .contact-list {
    position: absolute; left: 572px; top: 38px; list-style: none;
  }
  .contact-list li {
    display: flex; align-items: center; height: 33px;
    color: var(--text-light); font-size: 31px;
  }
  .contact-icon {
    width: 26px; margin-right: 18px; display: flex; justify-content: center;
    color: var(--accent-blue); font-size: 19px; font-weight: 600;
  }
  .contact-icon svg { display: block; }
</style>
</head>
<body>
  <div class="business-card">
    <div class="brand-area">
      <div class="brand-dot"></div>
      <div class="brand-name">DORLEY<br>PLUMBING</div>
    </div>
    <div class="accent-stripe"><span class="deep"></span><span class="light"></span></div>
    <div class="info-band">
      <div class="band-divider"></div>
      <div class="person">
        <p class="person-name">Mitch Dorley</p>
        <p class="person-role">Owner</p>
      </div>
      <ul class="contact-list">
        <li>
          <span class="contact-icon">
            <svg width="22" height="16" viewBox="0 0 22 16" fill="#2a9fd6"><path d="M1 5c0-3 4-4 10-4s10 1 10 4v2h-5V5H6v2H1z"/><rect x="4" y="8" width="14" height="7" rx="1.5"/></svg>
          </span>0455 318 726
        </li>
        <li>
          <span class="contact-icon">
            <svg width="14" height="22" viewBox="0 0 14 22" fill="none" stroke="#2a9fd6" stroke-width="2"><rect x="1" y="1" width="12" height="20" rx="2"/></svg>
          </span>0455 318 727
        </li>
        <li><span class="contact-icon">Fx</span>0455 318 728</li>
        <li>
          <span class="contact-icon">
            <svg width="20" height="14" viewBox="0 0 20 14"><rect width="20" height="14" rx="1.5" fill="#2a9fd6"/><path d="M1 1l9 7 9-7" fill="none" stroke="#0d1014" stroke-width="1.5"/></svg>
          </span>mitch@dorleymail.com
        </li>
      </ul>
    </div>
  </div>
</body>
</html>
```